K & T Fabrication Web Design | ||
Web Template | ||
Manufacturing | ||
www.kandtfab.example | ||
The current business that I am purchasing is a run of the mill, precision metal machining and manufacturing company. The owner is retirement age and it's my objective to make it new school and cutting edge. I want professional, eye catching concepts that capture what I am trying to do with the traditionally old school industry. I want to appeal to the younger engineers in the industry. I want to illustrate the professional, cutting edge services I intend to offer through my company. I want to show that we are not the traditional, dirty old machine shop. We are a company run by a young, fast-paced engineer focused on providing the highest quality work in the industry. | ||
I would like to have a navigation bar that contains "HOME", "CAPABILITIES", "PROJECTS", "ABOUT US", and "CONTACT US" tabs. I like un-cluttered websites that deliver a clear message that the company has an organized, structured leadership in place. I want to show that the machining industry is not always old, dirty, and antiquated. My company is cutting edge, engineering driven, and able to meet the customer's every demand. | ||
Cutting-Edge Unique/Creative Clean/Simple Professional Sophisticated Modern Industrial Progressive High Tech Masculine |
Black/Charcoal | ||
above header | ||
http://www.pellworth-clinical.example/ | ||
http://world.varnick-ostley.example/master/6600.htm | ||
http://brockmoorlifts.example/ | ||
Please attempt to match font type of the uploaded business card and company logo designs. I would like to have a seamless design throughout. | ||

```html
<!DOCTYPE html>
<html lang="en">
<head>
<meta charset="utf-8">
<title>K &amp; T Fabrication</title>
<link href="https://fonts.googleapis.com/css2?family=Arimo:wght@400;700&display=swap" rel="stylesheet">
<style>
:root{
  --blue:#1f7fc4;
  --blue-light:#3fa3e6;
  --navy:#0e2a44;
  --nav-top:#2b6fa6;
  --nav-bottom:#0f3f6b;
  --ink:#333;
  --muted:#6a6a6a;
  --panel:#e9ebee;
  --card:#ffffff;
  --line:#d2d6db;
  --footer:#0b0b0b;
  --footer-text:#bfbfbf;
}
*{box-sizing:border-box;margin:0;padding:0}
html,body{width:1200px;height:978px;overflow:hidden;background:#fff;font-family:"Arimo",Arial,sans-serif;color:var(--ink)}
.page{position:relative;width:1200px;height:978px}
.wrap{position:absolute;left:120px;width:960px}

/* header */
.header{top:0;height:135px}
.brand{position:absolute;left:0;top:40px;display:flex;align-items:center;gap:12px}
.brand-dot{width:44px;height:44px;border-radius:50%;background:var(--blue)}
.brand-name{font-size:30px;font-weight:700;color:var(--navy);letter-spacing:.5px}
.call{position:absolute;right:130px;top:58px;text-align:right}
.call-label{font-size:22px;font-weight:700;color:var(--blue)}
.call-number{font-size:24px;font-weight:700;color:#c0262d;margin-top:4px}
.agent{position:absolute;right:0;top:8px;width:120px;height:125px;border-radius:8px 8px 0 0;background:linear-gradient(180deg,#d9e3ec,#8aa4bd)}

/* nav */
.nav{top:137px;height:40px;background:linear-gradient(180deg,var(--nav-top),var(--nav-bottom));border-radius:4px;display:flex;align-items:center;padding:0 14px}
.nav a{color:#fff;text-decoration:none;font-size:15px;padding:0 22px;height:40px;line-height:40px;border-right:1px solid rgba(255,255,255,.25)}
.nav a.active{background:rgba(0,0,0,.25);font-weight:700}
.search{margin-left:auto;width:150px;height:24px;border-radius:12px;background:#fff;font-size:11px;color:#999;line-height:24px;padding-left:10px}

/* hero */
.hero{top:182px;height:222px;background:linear-gradient(180deg,#1a1d22,#050608);border-radius:4px;overflow:hidden}
.hero-photo{position:absolute;left:0;top:0;width:470px;height:222px;background:linear-gradient(135deg,#9aa5ae,#3d4a55 60%,#1c2530)}
.hero-copy{position:absolute;left:500px;top:26px;width:440px;color:#fff}
.hero-title{font-size:27px;font-weight:700;line-height:1.15;letter-spacing:.3px}
.hero-text{font-size:12px;line-height:1.45;color:#cfd5db;margin-top:12px}
.hero-btn{position:absolute;right:22px;bottom:20px;width:190px;height:40px;border-radius:20px;background:linear-gradient(180deg,var(--blue-light),#1565a3);color:#fff;font-size:17px;font-weight:700;display:flex;align-items:center;justify-content:space-between;padding:0 8px 0 30px}
.arrow{width:26px;height:26px;border-radius:50%;background:#fff;display:flex;align-items:center;justify-content:center}

/* content */
.content{top:412px;height:392px;background:var(--panel);border-radius:4px}
.card{position:absolute;background:var(--card);border:1px solid var(--line);border-radius:6px;padding:14px 18px;overflow:hidden}
.card-head{display:flex;align-items:center;gap:8px;font-size:17px;font-weight:700;color:var(--navy);margin-bottom:10px;white-space:nowrap}
.card-head .accent{color:var(--blue)}
.icon{width:22px;height:22px;border-radius:50%;background:var(--blue);flex:none}
.card p{font-size:11.5px;line-height:1.45;color:var(--muted);margin-bottom:8px}
.more{position:absolute;right:14px;bottom:10px;font-size:11px;color:var(--ink);display:flex;align-items:center;gap:6px;background:var(--card)}
.more i{width:14px;height:14px;border-radius:50%;background:var(--blue);display:inline-block}
.welcome{left:10px;top:12px;width:740px;height:168px}
.project{left:760px;top:12px;width:190px;height:168px;padding:14px 12px}
.project .card-head{font-size:15px;gap:6px}
.project-body{display:flex;gap:8px}
.project-thumb{flex:none;width:56px;height:86px;background:linear-gradient(180deg,#6f7b86,#2b3540)}
.project ul{list-style:disc;padding-left:11px;font-size:9px;color:var(--muted);line-height:1.3}
.project li{margin-bottom:4px}
.col{top:198px;width:300px;height:180px}
.col1{left:10px}.col2{left:330px}.col3{left:650px}

/* footer */
.footer{position:absolute;left:0;top:812px;width:1200px;height:166px;background:var(--footer)}
.f-links{position:absolute;left:120px;top:16px;font-size:13px;color:#fff}
.f-brand{position:absolute;left:120px;top:48px;display:flex;align-items:center;gap:8px;color:#fff;font-size:14px;font-weight:700}
.f-brand .brand-dot{width:26px;height:26px}
.f-copy{position:absolute;left:120px;top:92px;font-size:10px;color:var(--footer-text);line-height:1.5}
.f-sub{position:absolute;left:340px;top:84px}
.f-sub-title{font-size:16px;font-weight:700;color:#fff;display:flex;align-items:center;gap:8px}
.f-sub-form{display:flex;margin-top:12px}
.f-input{width:180px;height:22px;background:#fff;font-size:9px;color:#888;line-height:22px;padding-left:6px}
.f-btn{width:48px;height:22px;background:#e3e3e3;font-size:11px;line-height:22px;text-align:center;margin-left:4px}
.testimonial{position:absolute;left:620px;top:0;width:460px;height:166px;background:#050505;padding:14px 20px}
.t-head{display:flex;align-items:center;gap:10px;font-size:18px;color:#fff;letter-spacing:1px}
.t-head .sq{width:32px;height:32px;background:#fff}
.t-text{font-size:11.5px;line-height:1.45;color:#fff;margin-top:10px;padding-left:42px}
.t-more{position:absolute;right:20px;bottom:10px;font-size:11px;color:#fff;display:flex;align-items:center;gap:6px}
.t-more i{width:14px;height:14px;border-radius:50%;background:var(--blue);display:inline-block}
</style>
</head>
<body>
<div class="page">

  <header class="wrap header">
    <div class="brand"><span class="brand-dot"></span><span class="brand-name">K &amp; T FABRICATION</span></div>
    <div class="call">
      <div class="call-label">Call Us :</div>
      <div class="call-number">090 555 0142</div>
    </div>
    <div class="agent" role="img" aria-label="Photo of a customer service representative wearing a headset"></div>
  </header>

  <nav class="wrap nav">
    <a class="active" href="#">HOME</a>
    <a href="#">About Us</a>
    <a href="#">Capabilities</a>
    <a href="#">Projects</a>
    <a href="#">Contact Us</a>
    <div class="search">Search Here</div>
  </nav>

  <section class="wrap hero">
    <div class="hero-photo" role="img" aria-label="Photo of a precision machining plant with steel equipment"></div>
    <div class="hero-copy">
      <h1 class="hero-title">PRECISION PRODUCTS &amp;<br>ENGINEERED SOLUTION</h1>
      <p class="hero-text">Lorem Ipsum is simply dummy text of the printing and typesetting industry. Lorem Ipsum has been the industry's standard dummy text ever since the 1500s, when an unknown printer took a galley of type and scrambled it to make a type specimen book.</p>
    </div>
    <div class="hero-btn">LEARN MORE <span class="arrow"><svg width="12" height="12" viewBox="0 0 12 12"><path d="M4 2l4 4-4 4" stroke="#1f7fc4" stroke-width="2" fill="none"/></svg></span></div>
  </section>

  <main class="wrap content">
    <article class="card welcome">
      <div class="card-head"><span class="icon"></span>WELCOME TO <span class="accent">K &amp; T FABRICATION</span></div>
      <p>Lorem Ipsum is simply dummy text of the printing and typesetting industry. Lorem Ipsum has been the industry's standard dummy text ever since the 1500s, when an unknown printer took a galley of type and scrambled it to make a type specimen book. It has survived not only five centuries, but also the leap into electronic typesetting, remaining essentially unchanged.</p>
      <p>Lorem Ipsum is simply dummy text of the printing and typesetting industry. Lorem Ipsum has been the industry's standard dummy text ever since the 1500s.</p>
      <span class="more">Read More <i></i></span>
    </article>

    <aside class="card project">
      <div class="card-head"><span class="icon"></span>Current Project</div>
      <div class="project-body">
        <div class="project-thumb" role="img" aria-label="Photo of a current machining project"></div>
        <ul>
          <li>Lorem Ipsum is simply dummy text</li>
          <li>Lorem Ipsum is simply dummy text</li>
          <li>Lorem Ipsum is simply dummy text</li>
        </ul>
      </div>
      <span class="more">Read More <i></i></span>
    </aside>

    <article class="card col col1">
      <div class="card-head"><span class="icon"></span>WHY <span class="accent">K &amp; T</span></div>
      <p>Lorem Ipsum is simply dummy text of the printing and typesetting industry. Lorem Ipsum has been the industry's standard dummy text ever since the 1500s, when an unknown printer took a galley of type and scrambled it to make a type specimen book.</p>
      <span class="more">Read More <i></i></span>
    </article>

    <article class="card col col2">
      <div class="card-head"><span class="icon"></span><span class="accent">K &amp; T</span> CAPABILITES</div>
      <p>Lorem Ipsum is simply dummy text of the printing and type setting industry. Lorem Ipsum has been the industry's standard dummy text ever since the 1500s, when an unknown printer took a galley of type and scrambled it. Lorem Ipsum has been the industry's standard dummy text.</p>
      <span class="more">Read More <i></i></span>
    </article>

    <article class="card col col3">
      <div class="card-head"><span class="icon"></span><span class="accent">K &amp; T</span> ACTIVITY</div>
      <p>Lorem Ipsum is simply dummy text of the printing and typesetting industry. Lorem Ipsum has been the industry's standard dummy text ever since the 1500s, when an unknown printer took a galley of type and scrambled it to make a type specimen book.</p>
      <span class="more">Read More <i></i></span>
    </article>
  </main>

  <footer class="footer">
    <div class="f-links">Home | About Us | Capabilities | Projects | Contact Us</div>
    <div class="f-brand"><span class="brand-dot"></span>K &amp; T FABRICATION</div>
    <div class="f-copy">Copy right 2011, All rights reserved.<br>Licence agreement | Terms &amp; conditions</div>
    <div class="f-sub">
      <div class="f-sub-title"><span class="icon"></span>K &amp; T SUBSCRIPTION</div>
      <div class="f-sub-form"><div class="f-input">Type your Email Address</div><div class="f-btn">Enter</div></div>
    </div>
    <section class="testimonial">
      <div class="t-head"><span class="sq"></span>TESTIMONIAL</div>
      <p class="t-text">Lorem Ipsum is simply dummy text of the printing and type setting industry. Lorem Ipsum has been the industry's standard dummy text ever since the 1500s, when an unknown printer took a galley of type and scrambled it to make a type specimen book. Lorem Ipsum is simply dummy text of the printing and typesetting industry.</p>
      <span class="t-more">Read More <i></i></span>
    </section>
  </footer>

</div>
</body>
</html>
```